New Design for Willow Glow & Laser

The name of our company is Willow Glow & Laser, and this is our current website: www.WillowGlowLaser.example. We are looking for a fresh design mock-up of our website.
What is important to us?
> We want to maintain the same navigation.
> We want to use the same content (e.g., text, pictures, etc.)
> We want to maintain the color scheme.
> The website aims to get visitors to BOOK ONLINE or BUY ONLINE.
Essential instructions for designers:
> Please visit our current website and our social media accounts to get a better idea of our brand design.
> We want a mockup design for our home page, service page, pricing page, before & after page, shop deals page, careers page, contact pages, and blog pages.
> Color codes: #faa641, #222222, #fffffe, #ea8103
Target Market(s)
women 25 - 45
Number of Pages Required
5+ page
Look and feel

```html
<!DOCTYPE html>
<html lang="en">
<head>
<meta charset="utf-8">
<title>Willow Glow &amp; Laser — Home</title>
<link href="https://fonts.googleapis.com/css2?family=Rozha+One&family=Montserrat:wght@400;500;600;700&display=swap" rel="stylesheet">
<style>
:root{
  --orange:#faa641;
  --orange-deep:#ea8103;
  --ink:#222222;
  --white:#fffffe;
  --hero-bg:#efe9e3;
  --cream:#faf6f1;
  --muted:#555555;
  --stage:#f4f4f4;
  --black:#000000;
}
*{box-sizing:border-box;margin:0;padding:0}
html,body{width:1200px;height:2993px;overflow:hidden;background:var(--stage);font-family:"Montserrat",sans-serif;color:var(--ink)}
.page{position:absolute;left:0;top:128px;width:1200px;height:2737px;background:var(--white);overflow:hidden}
.abs{position:absolute}
.serif{font-family:"Rozha One",serif;font-weight:400}
.btn{position:absolute;display:flex;align-items:center;justify-content:center;gap:8px;background:var(--orange);color:var(--white);border-radius:30px;font-size:11px;font-weight:500;letter-spacing:.2px}
.photo{position:absolute;overflow:hidden}

/* nav */
.nav{position:absolute;left:0;top:0;width:1200px;height:45px;background:var(--white)}
.brand{position:absolute;display:flex;align-items:center;gap:6px;font-weight:700}
.brand .dot{width:14px;height:14px;border-radius:50%;background:var(--orange)}
.nav .brand{left:68px;top:13px;font-size:14px}
.nav-links{position:absolute;left:433px;top:16px;display:flex;gap:27px;font-size:11px}
.nav-links .active{color:var(--orange)}
.nav .btn{left:1017px;top:9px;width:122px;height:28px}

/* hero */
.hero{position:absolute;left:0;top:45px;width:1200px;height:533px;background:var(--hero-bg)}
.hero h1{position:absolute;left:192px;top:110px;font-size:56px;line-height:58px;color:var(--ink)}
.chip{display:inline-block;vertical-align:middle;border-radius:20px;background:linear-gradient(90deg,#c9b8a8,#3a302c)}
.hero .lede{position:absolute;left:192px;top:310px;font-size:13.5px;line-height:19px;color:#333}
.hero .btn{left:192px;top:385px;width:136px;height:37px}
.hero .deals{position:absolute;left:343px;top:398px;font-size:11px;text-decoration:underline}
.hero .photo{left:500px;top:0;width:700px;height:533px;background:linear-gradient(120deg,#d9cfc4 0%,#8a6d5a 45%,#2a2220 70%,#d8c3b0 100%)}
.badge{position:absolute;left:513px;top:379px;width:98px;height:98px;border-radius:50%;background:var(--white);box-shadow:0 4px 14px rgba(0,0,0,.12)}

/* about */
.arch{position:absolute;left:181px;top:650px;width:286px;height:396px;border:1.5px solid #999;border-radius:143px 143px 14px 14px}
.arch .photo{left:10px;top:-3px;width:276px;height:385px;border-radius:138px 138px 0 0;background:linear-gradient(160deg,#d8c7b8,#6b4f40 60%,#e9dccf)}
.pill-card{position:absolute;background:var(--white);border-radius:20px;box-shadow:0 4px 14px rgba(0,0,0,.12);display:flex;align-items:center;gap:6px;padding:4px 10px 4px 5px;font-size:8px}
.avatar{border-radius:50%;background:linear-gradient(135deg,#c6a58d,#5a4034)}
.stars{color:var(--orange);letter-spacing:2px}
.about h2{position:absolute;left:563px;top:700px;font-size:30px}
.about .body{position:absolute;left:563px;top:770px;width:455px;font-size:11.3px;line-height:19px;color:#333}
.about .body p{margin-bottom:18px}
.about .btn{left:556px;top:976px;width:134px;height:37px}

/* offer */
.offer-band{position:absolute;left:0;top:1132px;width:1200px;height:310px;background:var(--cream)}
.center-title{position:absolute;left:0;width:1200px;text-align:center}
.offer h2{top:1190px;font-size:30px}
.offer p{top:1236px;font-size:11.5px;color:#333}
.service{position:absolute;top:1302px;width:154px;height:232px;border-radius:77px;border:1.5px solid #888;overflow:hidden}
.service.feature{background:var(--orange);border-color:var(--orange);display:flex;align-items:center;justify-content:center;text-align:center;color:var(--white);font-size:18px;line-height:20px}

/* testimonials */
.testi h2{position:absolute;left:192px;top:1622px;font-size:30px}
.testi .sub{position:absolute;left:192px;top:1670px;font-size:11.5px;color:#333}
.arrow{position:absolute;top:1633px;width:28px;height:28px;border-radius:50%;border:1.2px solid var(--ink);display:flex;align-items:center;justify-content:center}
.arrow.off{border-color:#bbb}
.review{position:absolute;top:1752px;width:252px;height:216px;background:var(--white);box-shadow:0 4px 18px rgba(0,0,0,.08);border-radius:6px;text-align:center;padding:60px 30px 0}
.review .avatar{position:absolute;left:96px;top:-28px;width:60px;height:60px;border:3px solid var(--white)}
.review .quote{font-size:9.5px;line-height:15px;color:#555;height:78px}
.review .stars{font-size:11px;margin-top:6px}
.review .name{font-size:9.5px;font-weight:600;margin-top:12px}

/* contact band */
.cta{position:absolute;left:188px;top:2075px;width:813px;height:139px;background:var(--orange);border-radius:70px}
.cta h3{position:absolute;left:241px;top:2118px;font-size:22px;line-height:29px;color:var(--white)}
.cta-btn{position:absolute;left:573px;top:2126px;width:136px;height:37px;background:var(--white);border-radius:30px;display:flex;align-items:center;justify-content:center;gap:8px;font-size:10.5px;font-weight:600}
.cta-photo{position:absolute;left:770px;top:2028px;width:220px;height:186px;border-radius:90px 90px 0 0;background:linear-gradient(180deg,#3b2e2a,#1c1a1a 60%,#c9b29d)}

/* gallery */
.gallery{position:absolute;left:0;top:2307px;width:1200px;height:127px;display:flex;gap:7px}
.gallery div{flex:1}

/* footer */
.footer{position:absolute;left:0;top:2444px;width:1200px;height:293px;background:var(--black);color:var(--white)}
.footer .brand{left:200px;top:52px;font-size:22px}
.footer .brand .dot{width:20px;height:20px}
.footer .about-text{position:absolute;left:200px;top:114px;width:250px;font-size:10px;line-height:17px}
.social{position:absolute;left:200px;top:186px;display:flex;gap:11px}
.social span{width:20px;height:20px;border-radius:50%;border:1.2px solid var(--white)}
.footer .copy{position:absolute;left:200px;top:240px;font-size:9px}
.fcol{position:absolute;top:78px;font-size:10px;line-height:22.5px}
.fcol h4{font-size:11.5px;font-weight:600;margin-bottom:6px}
.news-input{position:absolute;left:848px;top:104px;width:158px;height:30px;border:1px solid var(--white);border-radius:20px;font-size:9px;padding:9px 15px}
.news-btn{position:absolute;left:848px;top:148px;width:158px;height:28px;background:var(--orange);border-radius:20px;color:var(--ink);font-size:9.5px;font-weight:600;display:flex;align-items:center;justify-content:center}
</style>
</head>
<body>
<main class="page">

  <header class="nav">
    <div class="brand"><span class="dot"></span>Willow Glow &amp; Laser</div>
    <nav class="nav-links">
      <span class="active">Home</span><span>Services</span><span>Pricing</span><span>About</span><span>Blog</span><span>Contact</span>
    </nav>
    <div class="btn">BOOK ONLINE</div>
  </header>

  <section class="hero">
    <h1 class="serif">Your skin <span class="chip" style="width:28px;height:28px;background:var(--orange)" role="img" aria-label="Small fruit accent"></span><br>
      <span class="chip" style="width:60px;height:32px" role="img" aria-label="Small photo of a facial treatment"></span> Deserves<br>
      Attention <span class="chip" style="width:52px;height:32px" role="img" aria-label="Small photo of a skincare treatment"></span></h1>
    <p class="lede">LASER CENTER &amp; MEDISPA located in<br>Downtown Phoenix, Tempe, Tucson, &amp; Yuma.</p>
    <div class="btn">BOOK ONLINE
      <svg width="18" height="8" viewBox="0 0 18 8"><path d="M0 4h16M13 1l3 3-3 3" stroke="#fffffe" fill="none" stroke-width="1.2"/></svg></div>
    <span class="deals">Shope Deals</span>
    <div class="photo" role="img" aria-label="Aesthetician holding a mirror beside a smiling client during a lip treatment"></div>
    <div class="badge">
      <svg width="98" height="98" viewBox="0 0 98 98">
        <circle cx="49" cy="49" r="34" fill="none" stroke="#222" stroke-width=".6" stroke-dasharray="3 3"/>
        <circle cx="49" cy="49" r="10" fill="none" stroke="#faa641" stroke-width="1.5"/>
        <path d="M44 58l-3 9 8-4 8 4-3-9" fill="none" stroke="#faa641" stroke-width="1.5"/>
      </svg>
    </div>
  </section>

  <section class="about">
    <div class="arch">
      <div class="photo" role="img" aria-label="Client with dark hair receiving a facial treatment"></div>
    </div>
    <div class="pill-card" style="left:165px;top:683px"><span class="avatar" style="width:22px;height:22px"></span><span class="stars" style="font-size:11px">★★★★★</span></div>
    <div class="pill-card" style="left:318px;top:1017px;width:196px;height:34px"><span class="avatar" style="width:24px;height:24px;flex:none"></span><span>Lorem Ipsum is simply dummy<br>text of the printing.</span></div>
    <h2 class="serif">About Willow Glow &amp; Laser</h2>
    <div class="body">
      <p>At Willow Glow &amp; Laser, we've always believed that caring about your skin and your appearance is not selfish, it is self-care. It's time to be proud of the steps you take to look your best and it's time you ask for the best. Your skin deserves it.</p>
      <p>Willow brings to you the latest technology, techniques, and the best professionals to deliver the results you want guaranteed. It's time to cross out the judgment, the labels, the hesitation, and the regrets.</p>
      <p>We offer clinic locations in Tucson, AZ, Phoenix, AZ, Tempe, AZ and Yuma, AZ.</p>
    </div>
    <div class="btn">BOOK ONLINE
      <svg width="18" height="8" viewBox="0 0 18 8"><path d="M0 4h16M13 1l3 3-3 3" stroke="#fffffe" fill="none" stroke-width="1.2"/></svg></div>
  </section>

  <section class="offer">
    <div class="offer-band"></div>
    <h2 class="serif center-title">What We Offer</h2>
    <p class="center-title">Lorem Ipsum is simply dummy text of the printing and typesetting industry</p>
    <div class="service" style="left:194px;background:linear-gradient(160deg,#e8d6c6,#a47c62 55%,#2b2421)" role="img" aria-label="Chemical peel facial treatment"></div>
    <div class="service" style="left:357px;background:linear-gradient(160deg,#caa98f,#7b5a46 50%,#f0e4d8)" role="img" aria-label="Close-up of eye area skincare"></div>
    <div class="service feature serif" style="left:521px">Laser Hair<br>Removal</div>
    <div class="service" style="left:685px;background:linear-gradient(180deg,#e8e4e0,#3a302c 55%,#cfc3b8)" role="img" aria-label="Technician performing a facial treatment"></div>
    <div class="service" style="left:848px;background:linear-gradient(160deg,#dcd6d2,#6e5446 50%,#e6cfbd)" role="img" aria-label="Injectable treatment with gloved hands"></div>
  </section>

  <section class="testi">
    <h2 class="serif">What Our Happy Clients Say</h2>
    <p class="sub">Lorem Ipsum is simply dummy text of the printing</p>
    <div class="arrow off" style="left:890px"><svg width="12" height="8" viewBox="0 0 12 8"><path d="M12 4H1M4 1L1 4l3 3" stroke="#bbb" fill="none"/></svg></div>
    <div class="arrow" style="left:920px"><svg width="12" height="8" viewBox="0 0 12 8"><path d="M0 4h11M8 1l3 3-3 3" stroke="#222" fill="none"/></svg></div>
    <div class="review" style="left:194px"><span class="avatar" role="img" aria-label="Client portrait"></span>
      <p class="quote">Awesome experience! Clean, professional, fast and painless laser hair removal services. Talia was a great technician and the whole experience was stress-free!</p>
      <div class="stars">★★★★★</div><div class="name">Marisa T</div></div>
    <div class="review" style="left:474px"><span class="avatar" role="img" aria-label="Client portrait"></span>
      <p class="quote">I have been going to Willow, for over a year and am very satisfied with the services and the staff.</p>
      <div class="stars">★★★★★</div><div class="name">Carla R</div></div>
    <div class="review" style="left:753px"><span class="avatar" role="img" aria-label="Client portrait"></span>
      <p class="quote">Talia is my technician and I love her! Always goes the extra mile to make sure areas are covered, and that I'm getting the best result. I couldn't be happier.</p>
      <div class="stars">★★★★★</div><div class="name">Nora B</div></div>
  </section>

  <section>
    <div class="cta"></div>
    <div class="cta-photo" role="img" aria-label="Staff member seated holding a hand mirror"></div>
    <h3 class="serif">If you have any questions,<br>Please contact us</h3>
    <div class="cta-btn">GET IN TOUCH
      <svg width="18" height="8" viewBox="0 0 18 8"><path d="M0 4h16M13 1l3 3-3 3" stroke="#222" fill="none" stroke-width="1.2"/></svg></div>
  </section>

  <section class="gallery">
    <div style="background:linear-gradient(135deg,#6d7a56,#d9c6b2)" role="img" aria-label="Two staff members holding products"></div>
    <div style="background:linear-gradient(135deg,#3a2c26,#caa48a)" role="img" aria-label="Close-up of clear skin"></div>
    <div style="background:linear-gradient(135deg,#d6d1cc,#2f2a28)" role="img" aria-label="Technician with treatment device"></div>
    <div style="background:linear-gradient(135deg,#e0dcd8,#2a2624)" role="img" aria-label="Staff member holding a mirror"></div>
    <div style="background:linear-gradient(135deg,#cfc9c4,#1f1c1b)" role="img" aria-label="Technician performing a treatment"></div>
    <div style="background:linear-gradient(135deg,#c48a5a,#e8e0d8)" role="img" aria-label="Team member assisting a client"></div>
  </section>

  <footer class="footer">
    <div class="brand"><span class="dot"></span>Willow Glow &amp; Laser</div>
    <p class="about-text">At Willow Glow &amp; Laser, we've always believed that caring about your skin and your appearance is not selfish, it is self-care.</p>
    <div class="social"><span></span><span></span><span style="border-color:var(--orange)"></span><span></span></div>
    <p class="copy">© 2024 Willow Glow &amp; Laser. All Rights Reserved.</p>
    <div class="fcol" style="left:520px"><h4>Links</h4>Home<br>Services<br>Pricing<br>About<br>Blog</div>
    <div class="fcol" style="left:690px"><h4>Get in Touch</h4>Our Locations<br>Send an email</div>
    <div class="fcol" style="left:848px"><h4>Newsletter</h4></div>
    <div class="news-input">Enter Your Email</div>
    <div class="news-btn">SUBSCRIBE</div>
  </footer>

</main>
</body>
</html>
```